Industrial Company needing new business cards

We are a newly branded Industrial trade company. We specialise in Electrical, Mechanical and Air-conditioning.

I would like to see designs single sided. Focusing on the color scheme white/red/black and possibly gray. Possibly make it a black card with white writting... but open to all designs.

I would like the design to be professional, sleek and to the point.

Industry/Entity Type

Business

Contact Information for Business Card

Tom Harwick
Managing Director / Electrician
tomwork@velnet.com.au
47 Garnet Road, Kelvale NSW 2318
Mobile: 0427115830
www.harwickindustrialgroup.com.au

Requirements
Must have
• Must be able to be sent in a manner that i can change the details for each employee.
• Our logo
Nice to have
• Would like it to somehow have " incorporating Talvo Group Pty Ltd" as this is the company we have taken over.
Should not have
• No yellow!!!
• must not simply place "talvo group" randomly on the business card. refer nice to have.

```html
<!DOCTYPE html>
<html lang="en">
<head>
<meta charset="utf-8">
<title>Harwick Industrial Group – Business Cards</title>
<link rel="stylesheet" href="https://fonts.googleapis.com/css2?family=Lato:wght@400;700;900&family=Questrial&display=swap">
<style>
  :root {
    --red: #e01f26;
    --black: #0b0b0b;
    --white: #ffffff;
    --panel: #f4f4f4;
    --grey: #555555;
    --stage: #e9e6e1;
  }
  * { box-sizing: border-box; margin: 0; padding: 0; }
  html, body { width: 1200px; height: 800px; overflow: hidden; }
  body {
    background: var(--stage);
    font-family: "Lato", sans-serif;
    display: flex;
    align-items: center;
    justify-content: center;
    gap: 60px;
  }
  .card {
    width: 525px;
    height: 300px;
    position: relative;
    overflow: hidden;
    box-shadow: 0 6px 18px rgba(0,0,0,.18);
  }

  /* Front */
  .card-front { background: var(--red); }
  .front-panel {
    position: absolute;
    left: 36px; top: 34px; right: 36px; bottom: 34px;
    background: var(--panel);
    display: flex;
    flex-direction: column;
    justify-content: space-between;
  }
  .front-brand { padding: 34px 0 0 46px; }
  .front-rule { height: 4px; background: var(--red); }
  .front-incorporating {
    font-family: "Questrial", sans-serif;
    font-size: 20px;
    color: var(--black);
    text-align: right;
    padding: 8px 16px 12px 0;
  }

  /* Brand name block */
  .brand { display: flex; align-items: center; gap: 12px; }
  .brand-mark { width: 22px; height: 22px; background: var(--red); flex: none; }
  .brand-text { display: flex; flex-direction: column; }
  .brand-name {
    font-weight: 900;
    text-transform: uppercase;
    color: var(--black);
    line-height: 1;
    letter-spacing: .5px;
  }
  .brand-services {
    font-size: 8px;
    text-transform: uppercase;
    letter-spacing: 1px;
    color: var(--grey);
    margin-top: 6px;
  }
  .front-brand .brand-name { font-size: 28px; }
  .back-brand .brand-name { font-size: 18px; }
  .back-brand .brand-mark { width: 16px; height: 16px; }
  .back-brand .brand-services { font-size: 6.5px; margin-top: 4px; }

  /* Back */
  .card-back { background: var(--black); }
  .back-top {
    height: 132px;
    background: var(--white);
    position: relative;
  }
  .back-brand { position: absolute; left: 28px; top: 28px; }
  .back-person {
    position: absolute;
    right: 26px; top: 88px;
    text-align: right;
  }
  .person-name {
    font-size: 17px;
    font-weight: 900;
    text-transform: uppercase;
    color: var(--black);
    letter-spacing: .3px;
  }
  .person-name .surname { color: var(--red); }
  .person-role {
    font-size: 10.5px;
    text-transform: uppercase;
    color: var(--grey);
    letter-spacing: .4px;
    margin-top: 2px;
  }
  .contact-list {
    list-style: none;
    position: absolute;
    left: 0; top: 0;
    padding-top: 18px;
  }
  .contact-item {
    display: flex;
    align-items: stretch;
    height: 38px;
    margin-bottom: 6px;
  }
  .contact-icon {
    width: 30px;
    background: var(--red);
    display: flex;
    align-items: center;
    justify-content: center;
    clip-path: polygon(0 0, 70% 0, 100% 50%, 70% 100%, 0 100%);
  }
  .contact-icon svg { width: 13px; height: 13px; fill: var(--white); }
  .contact-bar {
    width: 232px;
    margin-left: 4px;
    background: var(--red);
    color: var(--white);
    font-size: 10.5px;
    line-height: 1.3;
    display: flex;
    flex-direction: column;
    justify-content: center;
    padding-left: 22px;
    clip-path: polygon(0 0, 100% 0, 100% 100%, 0 100%, 12px 50%);
  }
  .back-bottom { position: relative; height: 168px; }
</style>
</head>
<body>

  <section class="card card-front" aria-label="Business card front">
    <div class="front-panel">
      <div class="front-brand brand">
        <span class="brand-mark"></span>
        <span class="brand-text">
          <span class="brand-name">Harwick Industrial Group</span>
          <span class="brand-services">Electrical - Mechanical - Airconditioning</span>
        </span>
      </div>
      <div>
        <div class="front-rule"></div>
        <p class="front-incorporating">incorporating Talvo Group Pty Ltd</p>
      </div>
    </div>
  </section>

  <section class="card card-back" aria-label="Business card back">
    <div class="back-top">
      <div class="back-brand brand">
        <span class="brand-mark"></span>
        <span class="brand-text">
          <span class="brand-name">Harwick Industrial Group</span>
          <span class="brand-services">Electrical - Mechanical - Airconditioning</span>
        </span>
      </div>
      <div class="back-person">
        <p class="person-name">Tom <span class="surname">Harwick</span></p>
        <p class="person-role">Managing Director / Electrician</p>
      </div>
    </div>
    <div class="back-bottom">
      <ul class="contact-list">
        <li class="contact-item">
          <span class="contact-icon">
            <svg viewBox="0 0 24 24"><path d="M6.6 10.8a15.1 15.1 0 0 0 6.6 6.6l2.2-2.2a1 1 0 0 1 1-.25 11.4 11.4 0 0 0 3.6.57 1 1 0 0 1 1 1V20a1 1 0 0 1-1 1A17 17 0 0 1 3 4a1 1 0 0 1 1-1h3.5a1 1 0 0 1 1 1c0 1.25.2 2.45.57 3.57a1 1 0 0 1-.25 1z"/></svg>
          </span>
          <span class="contact-bar">Mobile: 0427115830</span>
        </li>
        <li class="contact-item">
          <span class="contact-icon">
            <svg viewBox="0 0 24 24"><path d="M12 2a10 10 0 1 0 0 20 10 10 0 0 0 0-20zm6.9 6h-2.9a15.7 15.7 0 0 0-1.4-3.6A8 8 0 0 1 18.9 8zM12 4a14 14 0 0 1 1.9 4h-3.8A14 14 0 0 1 12 4zM4.3 14a8 8 0 0 1 0-4h3.4a16 16 0 0 0 0 4zm.8 2h2.9a15.7 15.7 0 0 0 1.4 3.6A8 8 0 0 1 5.1 16zM8 8H5.1a8 8 0 0 1 4.3-3.6A15.7 15.7 0 0 0 8 8zm4 12a14 14 0 0 1-1.9-4h3.8A14 14 0 0 1 12 20zm2.3-6H9.7a14.7 14.7 0 0 1 0-4h4.6a14.7 14.7 0 0 1 0 4zm.3 5.6a15.7 15.7 0 0 0 1.4-3.6h2.9a8 8 0 0 1-4.3 3.6zM16.3 14a16 16 0 0 0 0-4h3.4a8 8 0 0 1 0 4z"/></svg>
          </span>
          <span class="contact-bar">tomwork@velnet.com.au<br>www.harwickindustrialgroup.com.au</span>
        </li>
        <li class="contact-item">
          <span class="contact-icon">
            <svg viewBox="0 0 24 24"><path d="M12 2a7 7 0 0 0-7 7c0 5.2 7 13 7 13s7-7.8 7-13a7 7 0 0 0-7-7zm0 9.5A2.5 2.5 0 1 1 12 6.5a2.5 2.5 0 0 1 0 5z"/></svg>
          </span>
          <span class="contact-bar">47 Garnet Road,<br>Kelvale NSW 2318</span>
        </li>
      </ul>
    </div>
  </section>

</body>
</html>
```